Quorlan.com (Dedicated servers Provider)

We provide dedicated servers for clients around the world. We have created a layout for you. You need to create exactly the design based on these sketches. All text, you can take from our sketches (later we will replace them).

Target Market(s)

Web site owners and web developers

Requirements
Should not have
• The design should not use old-style fonts.

```html
<!DOCTYPE html>
<html lang="en">
<head>
<meta charset="utf-8">
<title>Quorlan.com – Dedicated Servers</title>
<link href="https://fonts.googleapis.com/css2?family=Arimo:wght@400;700&family=Oswald:wght@500&family=Caveat:wght@400&display=swap" rel="stylesheet">
<style>
:root{
  --page:#141414;
  --black:#0c0c0c;
  --green:#8cc21f;
  --green-dark:#6a9a10;
  --green-light:#a6d634;
  --ink:#1e1e1e;
  --muted:#555;
  --panel:#ececec;
  --white:#fff;
  --grey-band:#c9c9c9;
}
*{margin:0;padding:0;box-sizing:border-box}
html,body{width:960px;height:1200px;overflow:hidden}
body{background:var(--page);font-family:"Arimo",Arial,sans-serif;color:var(--ink);position:relative}
.abs{position:absolute}
a{color:inherit}

/* top bar */
.topbar{left:0;top:0;width:960px;height:16px;background:var(--black);font-size:8px;font-weight:700}
.topbar .questions{left:190px;top:4px;color:var(--green)}
.topbar .hotline{left:690px;top:3px;color:#eee;font-size:9px}
.sq{display:inline-block;width:8px;height:8px;background:var(--green);vertical-align:-1px;margin-right:4px;border-radius:1px}

/* header */
.header{left:190px;top:18px;width:580px;height:52px;background:linear-gradient(#fff,#dcdcdc)}
.logo{left:16px;top:12px;font-size:26px;font-weight:700;color:#333;letter-spacing:-0.5px}
.logo .mark{display:inline-block;width:22px;height:22px;background:#333;margin-right:6px;vertical-align:-3px}
.pill{top:14px;height:18px;border-radius:9px;background:linear-gradient(#3a3a3a,#111);color:#eee;font-size:7px;line-height:18px;padding:0 22px 0 11px}
.pill::after{content:"";position:absolute;right:6px;top:4px;width:10px;height:10px;border-radius:2px;background:var(--green)}

/* nav */
.nav{left:190px;top:70px;width:580px;height:25px;background:linear-gradient(var(--green-light),var(--green-dark));display:flex}
.nav span{font-size:7.5px;font-weight:700;color:#fff;line-height:25px;text-align:center;border-right:1px solid #5f8a0d}
.nav .home{background:#1b1b1b;width:46px}
.nav .order{margin-left:auto;background:linear-gradient(#333,#111);width:120px;font-size:11px;border:0}
.announce{left:190px;top:95px;width:580px;height:18px;background:#111;color:#ddd;font-size:7px;line-height:18px}
.announce .msg{left:46px}
.announce .msg a{color:var(--green)}
.announce .follow{left:492px;font-family:"Caveat",cursive;font-size:10px;color:#ccc}
.dot{display:inline-block;width:10px;height:10px;border-radius:50%;background:#fff;margin-left:2px;vertical-align:-2px}

/* hero */
.hero{left:190px;top:113px;width:580px;height:151px;background:linear-gradient(90deg,#2a2a2a,#4a4a4a 60%,#303030)}
.hero .heading{left:22px;top:14px;width:195px}
.hero h1{font-family:"Oswald",sans-serif;font-size:22px;color:#e6e6e6;font-weight:500;letter-spacing:0.2px;line-height:26px;white-space:nowrap}
.hero .from{display:block;text-align:right;font-size:7px;color:#bbb;margin-top:-1px}
.hero ul{left:22px;top:52px;list-style:none;font-size:9.5px;color:#eee;line-height:14px}
.hero li::before{content:"";display:inline-block;width:6px;height:6px;border-radius:50%;background:#eee;margin-right:5px}
.btn-dark{left:35px;top:125px;width:76px;height:16px;border-radius:8px;background:linear-gradient(#444,#111);border:1px solid #888;color:#fff;font-size:7px;text-align:center;line-height:14px}
.hero .quote{left:370px;top:24px;width:124px;font-family:"Caveat",cursive;font-size:12.5px;color:#ddd;line-height:21px;white-space:nowrap}
.hero .site{left:410px;top:89px;width:86px;text-align:right;font-size:7px;color:#ddd}
.hero-photo{left:500px;top:0;width:80px;height:151px;background:linear-gradient(#6d6d6d,#c9c4bd 55%,#e8e8e8)}
.tower{left:420px;top:118px;width:130px;height:174px;background:linear-gradient(90deg,#777,#e6e6e6 40%,#bdbdbd 70%,#888);border-radius:6px}

/* green band */
.band{left:190px;top:264px;width:580px;height:38px;background:linear-gradient(var(--green-light),var(--green-dark))}
.band .icon{left:10px;top:6px;width:22px;height:26px;background:#3b3b3b;border-radius:3px}
.band .hiring{left:34px;top:8px;font-size:11px;font-weight:700;color:#111}
.band .hiring small{display:block;font-size:7px;font-weight:400;text-decoration:underline}
.band .sales{right:6px;top:12px;font-family:"Caveat",cursive;font-size:15px;color:#111}
.band .sales b{font-family:"Arimo",sans-serif;font-size:11px;color:#fff}

/* content */
.content{left:190px;top:302px;width:580px;height:518px;background:var(--panel)}
.tab{top:14px;height:20px;font-size:7.5px;line-height:20px;text-align:center;color:#666;background:linear-gradient(#e0e0e0,#cfcfcf);border-radius:3px 3px 0 0}
.tab.active{background:#fff;color:#111;font-weight:700}
.plans{left:12px;top:34px;width:556px;height:202px;background:#fff;border-bottom:2px solid #ccc}
.plan{top:0;width:185px;height:200px}
.plan + .plan{border-left:1px solid #ddd}
.plan h3{position:absolute;top:20px;width:100%;text-align:center;font-size:10px;font-weight:700;color:#222}
.plan .box{position:absolute;left:34px;top:32px;width:116px;height:70px;background:linear-gradient(#e5e5e5,#9a9a9a 35%,#2a2a2a 40%,#111);border-radius:4px}
.plan .from{position:absolute;left:12px;top:110px;font-size:5.5px;color:#444}
.plan .price{position:absolute;left:2px;top:116px;font-size:12px;color:#222}
.plan .price b{font-size:24px;color:var(--green);font-weight:700}
.plan .price sup{font-size:12px;vertical-align:10px}
.plan .per{position:absolute;left:60px;top:136px;font-size:5.5px}
.plan .specs{position:absolute;left:88px;top:108px;font-size:7px;line-height:12px;color:#333}
.plan .select{position:absolute;left:56px;top:145px;width:75px;height:10px;border:1px solid #bbb;font-size:6px;line-height:8px;padding-left:3px}
.plan .all{position:absolute;left:2px;top:163px;font-size:6px;color:var(--green-dark);text-decoration:underline}
.plan .order{position:absolute;left:68px;top:158px;width:52px;height:18px;border-radius:9px;background:#111;color:#fff;font-size:7px;text-align:center;line-height:18px}

.map{left:22px;top:246px;width:116px;height:72px;background:radial-gradient(ellipse at 45% 40%,#49b6e0,#a7c9d6 60%,#e0e0e0 75%);border-radius:30px 20px 30px 40px}
.map-cap{left:36px;top:326px;font-size:5.5px;color:#333}
.check{font-size:10px;font-weight:700;color:#111}
.check svg{vertical-align:-4px;margin-right:6px}

.quotebox{left:12px;top:338px;width:556px;height:126px;background:#fff;border-bottom:2px solid #ccc}
.quotebox .mark{position:absolute;font-size:60px;color:#e4e4e4;font-weight:700;line-height:1}
.quotebox p{position:absolute;left:50px;top:26px;width:460px;text-align:center;font-size:14.5px;font-weight:700;color:#555;line-height:17.5px}
.quotebox .who{position:absolute;top:107px;width:100%;text-align:center;font-size:7px;font-weight:700}
.badge{top:480px;height:20px;background:#d2d2d2;border-radius:3px}

/* features */
.features{left:190px;top:820px;width:580px;height:244px;background:var(--grey-band)}
.features h2{position:absolute;left:6px;top:10px;font-size:11.5px;font-weight:700;color:#111}
.feat{width:190px}
.feat svg{position:absolute;left:0;top:0}
.feat h4{position:absolute;left:56px;top:6px;font-size:7.5px;font-weight:700;color:#111}
.feat p{position:absolute;left:56px;top:15px;width:140px;font-size:6.2px;color:#555;line-height:8px}
.rule{left:0;top:160px;width:580px;border-top:1px dashed #999}
.stat{top:198px}
.stat b{font-size:16px;font-weight:700;color:#111;line-height:18px}
.stat b::before{content:"";display:inline-block;width:6px;height:6px;border-radius:50%;border:1px solid #666;margin-right:3px;vertical-align:6px}
.stat small{display:block;font-size:6.2px;color:#444;margin:2px 0 0 12px;line-height:8px}

/* footer */
.footer{left:0;top:1064px;width:960px;height:136px;background:var(--page);color:#ddd}
.footer h5{position:absolute;top:12px;font-size:8px;font-weight:700;color:#fff}
.footer p{position:absolute;font-size:6.5px;line-height:8.5px}
.links{list-style:none;font-size:7px;line-height:11.5px}
.links li::before{content:"";display:inline-block;width:6px;height:6px;border-radius:50%;background:#ddd;margin-right:5px;vertical-align:-1px}
.vsep{top:10px;height:115px;border-left:1px solid #2a2a2a}
.bigphone{left:585px;top:66px;font-size:17px;font-weight:700;color:#fff}
.soc{top:98px;height:10px;background:#e8e8e8;color:#2a4a8a;font-size:5.5px;line-height:10px;padding:0 4px;border-radius:2px}
</style>
</head>
<body>

<div class="abs topbar">
  <span class="abs questions"><span class="sq"></span>Questions</span>
  <span class="abs hotline"><span class="sq"></span>0.800.000.RACK</span>
</div>

<header class="abs header">
  <div class="abs logo"><span class="mark"></span>Quorlan.com</div>
  <span class="abs pill" style="left:276px">User Registration</span>
  <span class="abs pill" style="left:376px">Customer Login</span>
  <span class="abs pill" style="left:476px">Live Chat Online</span>
</header>

<nav class="abs nav">
  <span class="home">HOME</span>
  <span style="width:70px">DOMAIN</span>
  <span style="width:92px">WEB HOSTING</span>
  <span style="width:92px">LATEST NEWS</span>
  <span style="width:90px">MY ACCOUNT</span>
  <span style="width:68px">CONTACT</span>
  <span class="order">ORDER NOW!</span>
</nav>
<div class="abs announce">
  <span class="abs msg"><span class="sq" style="background:#ddd"></span>Got an Important announcement or a special offer? Tell your customers about it! &nbsp;<a>readmore →</a></span>
  <span class="abs follow">Follow us <span class="dot"></span><span class="dot"></span><span class="dot"></span></span>
</div>

<section class="abs hero">
  <div class="abs heading">
    <h1>DEDICATED SERVERS</h1>
    <span class="from">FROM FASTNODE</span>
  </div>
  <ul class="abs">
    <li>Self-owned data centre</li>
    <li>24 x 7 x 365 on-site support</li>
    <li>100% uptime guarantee</li>
    <li>Industry leading control panel</li>
    <li>Custom servers; 24 hour setup</li>
  </ul>
  <span class="abs btn-dark">Find Out More</span>
  <p class="abs quote">Glad I managed to choose<br>one of the few companies<br>with good customer service</p>
  <span class="abs site">trailkit.co.uk</span>
  <div class="abs hero-photo" role="img" aria-label="Photo of a smiling customer in glasses"></div>
</section>

<section class="abs band">
  <div class="abs icon"></div>
  <div class="abs hiring">We are hiring<small>Apply online now</small></div>
  <div class="abs sales">Call Sales Today : <b>01632 960 210</b></div>
</section>
<div class="abs tower" role="img" aria-label="Two silver server tower units"></div>

<main class="abs content">
  <span class="abs tab active" style="left:12px;width:90px">Dedicated Servers</span>
  <span class="abs tab" style="left:106px;width:72px">Web Hosting</span>
  <span class="abs tab" style="left:183px;width:113px">Virtual Private Servers</span>

  <div class="abs plans">
    <div class="abs plan" style="left:4px">
      <h3>Corvex 4 2.4GHz</h3><div class="box"></div>
      <span class="from">Plans starting at</span>
      <span class="price">$<b>39</b><sup>00</sup></span><span class="per">Per mo.</span>
      <div class="specs">80GB SATA HD<br>1GB RAM<br>1TB Bandwidth</div>
      <div class="select">1 year - 39.00/mo</div>
      <span class="all">All Dedicated Servers</span><span class="order">ORDER</span>
    </div>
    <div class="abs plan" style="left:193px">
      <h3>Corvex 4 2.4GHz</h3><div class="box"></div>
      <span class="from">Plans starting at</span>
      <span class="price">$<b>39</b><sup>00</sup></span><span class="per">Per mo.</span>
      <div class="specs">80GB SATA HD<br>1GB RAM<br>1TB Bandwidth</div>
      <div class="select">1 year - 39.00/mo</div>
      <span class="all">All Dedicated Servers</span><span class="order">ORDER</span>
    </div>
    <div class="abs plan" style="left:384px">
      <h3>Corvex 4 2.4GHz</h3><div class="box"></div>
      <span class="from">Plans starting at</span>
      <span class="price">$<b>39</b><sup>00</sup></span><span class="per">Per mo.</span>
      <div class="specs">80GB SATA HD<br>1GB RAM<br>1TB Bandwidth</div>
      <div class="select">1 year - 39.00/mo</div>
      <span class="all">All Dedicated Servers</span><span class="order">ORDER</span>
    </div>
  </div>

  <div class="abs map" role="img" aria-label="Map of the network backbone across the country"></div>
  <span class="abs map-cap">Now offering ControlDesk Panel 11</span>

  <svg width="0" height="0" style="position:absolute"><defs><symbol id="tick" viewBox="0 0 20 16"><path d="M2 8l5 6L18 1" fill="none" stroke="#8cc21f" stroke-width="3.5" stroke-linecap="round"/></symbol></defs></svg>
  <span class="abs check" style="left:186px;top:258px"><svg width="18" height="15"><use href="#tick"/></svg>100 % Network Uptime SLA</span>
  <span class="abs check" style="left:186px;top:283px"><svg width="18" height="15"><use href="#tick"/></svg>ISO 9001 : 2008 Certified</span>
  <span class="abs check" style="left:186px;top:308px"><svg width="18" height="15"><use href="#tick"/></svg>24/7ITIL Technical Support</span>
  <span class="abs check" style="left:372px;top:258px"><svg width="18" height="15"><use href="#tick"/></svg>3 SSAE-16 Certified Data Centers</span>
  <span class="abs check" style="left:372px;top:283px"><svg width="18" height="15"><use href="#tick"/></svg>Coast-to-Coast IP Backbone</span>
  <span class="abs check" style="left:372px;top:308px"><svg width="18" height="15"><use href="#tick"/></svg>Award Winning Since 1996</span>

  <div class="abs quotebox">
    <span class="mark" style="left:6px;top:4px">“</span>
    <span class="mark" style="right:10px;top:90px">”</span>
    <p>We Had been Badly let down by several companies over the last few years, but last year i found hostmeadow.com on the web &amp; within 15 minutes i had received a response back from Martin with full pricing &amp; my server is still running perfectly, with no downtime</p>
    <span class="who">Sam Reed pixelhaul.com</span>
  </div>

  <span class="abs badge" style="left:38px;width:30px"></span>
  <span class="abs badge" style="left:92px;width:16px"></span>
  <span class="abs badge" style="left:132px;width:38px"></span>
  <span class="abs badge" style="left:196px;width:44px"></span>
  <span class="abs badge" style="left:259px;width:40px"></span>
  <span class="abs badge" style="left:322px;width:28px;border-radius:50%"></span>
  <span class="abs badge" style="left:378px;width:34px"></span>
  <span class="abs badge" style="left:432px;width:42px"></span>
  <span class="abs badge" style="left:494px;width:32px"></span>
</main>

<section class="abs features">
  <h2>SwiftRack - The Smart Choice For Dedicated Servers</h2>

  <div class="abs feat" style="left:6px;top:40px">
    <svg width="50" height="40" viewBox="0 0 50 40"><rect x="0" y="14" width="32" height="18" rx="2" fill="#111"/><g fill="#ccc"><rect x="3" y="17" width="4" height="3"/><rect x="9" y="17" width="4" height="3"/><rect x="15" y="17" width="4" height="3"/><rect x="21" y="17" width="4" height="3"/><rect x="3" y="22" width="4" height="3"/><rect x="9" y="22" width="4" height="3"/><rect x="15" y="22" width="4" height="3"/><rect x="21" y="22" width="4" height="3"/><rect x="5" y="27" width="20" height="2"/></g><rect x="36" y="10" width="14" height="22" rx="7" fill="#111"/><path d="M43 10 Q40 2 32 4" stroke="#111" fill="none" stroke-width="1.5"/></svg>
    <h4>Business-Class Ardent Hardware</h4>
    <p>We use high-end Ardent hardware, robust and reliable for building your ideal server.</p>
  </div>
  <div class="abs feat" style="left:210px;top:40px">
    <svg width="44" height="40" viewBox="0 0 44 40"><circle cx="20" cy="20" r="18" fill="#111"/><path d="M8 14q6-4 10 0t4 8q-4 6-10 2zM24 8q8 2 10 10-6 2-8-4z" fill="#c9c9c9"/></svg>
    <h4 style="left:50px">99.9% Uptime SLA</h4>
    <p style="left:50px">A fully redundant network and infrastructure backed up by our 99.9% Uptime Guarantee.</p>
  </div>
  <div class="abs feat" style="left:398px;top:40px">
    <svg width="44" height="40" viewBox="0 0 44 40"><path d="M2 4h34v24H14l-8 8v-8H2z" fill="#111"/><g fill="#fff"><circle cx="11" cy="16" r="2"/><circle cx="17" cy="16" r="2"/><circle cx="23" cy="16" r="2"/><circle cx="29" cy="16" r="2"/></g></svg>
    <h4 style="left:40px">99.9% Uptime SLA</h4>
    <p style="left:40px">A fully redundant network and infrastructure backed up by our 99.9% Uptime Guarantee.</p>
  </div>
  <div class="abs feat" style="left:16px;top:108px">
    <svg width="44" height="44" viewBox="0 0 44 44"><path d="M2 2h26l-8 8 20 20-10 10-20-20-8 8z" fill="#111"/></svg>
    <h4 style="left:52px">Fast Setup</h4>
    <p style="left:44px">We use high-end Ardent hardware, robust and reliable for building your ideal server.</p>
  </div>
  <div class="abs feat" style="left:210px;top:108px">
    <svg width="40" height="40" viewBox="0 0 40 40"><circle cx="20" cy="12" r="8" fill="#111"/><path d="M4 36q0-14 16-14t16 14z" fill="#111"/></svg>
    <h4 style="left:50px">Dedicated Account Manager</h4>
    <p style="left:50px">We use high-end Ardent hardware, robust and reliable for building your ideal server.</p>
  </div>
  <div class="abs feat" style="left:398px;top:108px">
    <svg width="40" height="40" viewBox="0 0 40 40"><path d="M8 18a12 12 0 0 1 22-6" stroke="#111" stroke-width="6" fill="none"/><path d="M26 4l10 4-4 10z" fill="#111"/><path d="M32 22a12 12 0 0 1-22 6" stroke="#111" stroke-width="6" fill="none"/><path d="M14 36l-10-4 4-10z" fill="#111"/></svg>
    <h4 style="left:40px">Simple Customization</h4>
    <p style="left:40px">A fully redundant network and infrastructure backed up by our 99.9% Uptime Guarantee.</p>
  </div>

  <div class="abs rule"></div>
  <h2 style="top:170px">Swift Rack is part of the Norvale Group - check out our stats!</h2>
  <div class="abs stat" style="left:14px"><b>1,800,000</b><small>domains registered in<br>over 250 extensions</small></div>
  <div class="abs stat" style="left:174px"><b>40,000</b><small>domains registered in<br>over 250 extensions</small></div>
  <div class="abs stat" style="left:330px"><b>500,000</b><small>domains registered in<br>over 250 extensions</small></div>
  <div class="abs stat" style="left:492px"><b>490,000</b><small>domains registered in<br>over 250 extensions</small></div>
</section>

<footer class="abs footer">
  <h5 style="left:190px">Keep it simple!</h5>
  <p style="left:190px;top:32px;width:130px">The web changes people and the things they do. This is why we develop increasingly reliable, easy-to-use and intuitive services.</p>
  <p style="left:190px;top:76px;text-decoration:underline">Learn more about SwiftRack</p>
  <div class="abs vsep" style="left:333px"></div>
  <h5 style="left:358px">About SwiftRack</h5>
  <ul class="abs links" style="left:358px;top:30px"><li>About Us</li><li>Contact Us</li><li>Terms &amp; Conditions</li></ul>
  <ul class="abs links" style="left:447px;top:30px"><li>Support</li><li>Why Choose Us</li><li>Service Legal Agreement</li></ul>
  <p style="left:358px;top:76px">Copyright © Quorlan.com 2012, All rights reserved!</p>
  <div class="abs vsep" style="left:562px"></div>
  <h5 style="left:585px">Information</h5>
  <p style="left:585px;top:32px;width:190px">Contact us via Support Ticket System in your Online Control Panel or alternatively call us on the number below:</p>
  <div class="abs bigphone">+44 (0)1632 960 458</div>
  <span class="abs soc" style="left:586px">Share 25</span>
  <span class="abs soc" style="left:637px">Follow @swiftrack</span>
  <span class="abs soc" style="left:586px;top:114px;color:#a33">Rec</span>
  <p style="left:610px;top:116px;color:#aaa">+44 &nbsp;&nbsp;&nbsp;&nbsp;Recomended this on the web</p>
</footer>

</body>
</html>
```